Black Friday for Baby Boutique

I need a flyer for my Black Friday and Local Loot Saturday events.

Entire store will be 30% off.

Friday hours: 9-6
Saturday: 9-4

Each customer will receive a coupon for December 1-24.

First 25 customers each day will receive a surprise gift valued at $50+

TONS of giveaways, food & drinks!

Bring/Buy an unopened toy for Pinecrest Mutual Aid & receive a $10 gift card.

Cloverpatch Cradle
Fernhollow, WA
Halvorn Plaza Center : Next to Tall Oats
(555) 201-4938

```html
<!DOCTYPE html>
<html lang="en">
<head>
<meta charset="utf-8">
<title>Cloverpatch Cradle – Black Friday Flyer</title>
<link rel="stylesheet" href="https://fonts.googleapis.com/css2?family=Bebas+Neue&family=Montserrat:wght@700&family=Oswald:wght@500;600&display=swap">
<style>
  :root {
    --page: #eeeeee;
    --red-deep: #8e0f22;
    --red-mid: #c8102e;
    --red-bright: #e31b3d;
    --gold-light: #fbe38a;
    --gold: #e2b43a;
    --gold-dark: #b98a1e;
    --silver: #e8e8ea;
    --ink: #141414;
    --white: #ffffff;
    --gift: #f3e6e6;
  }
  * { margin: 0; padding: 0; box-sizing: border-box; }
  html, body { width: 1200px; height: 1200px; overflow: hidden; background: var(--page); }
  .flyer {
    position: absolute; left: 190px; top: 18px; width: 820px; height: 1164px; overflow: hidden;
    background: radial-gradient(ellipse 70% 55% at 50% 45%, var(--red-bright) 0%, var(--red-mid) 45%, var(--red-deep) 100%);
    box-shadow: 0 6px 18px rgba(0,0,0,.25);
    font-family: "Bebas Neue", sans-serif; text-align: center;
  }
  .decor { position: absolute; }
  .decor-stars-left { left: 0; top: 60px; width: 110px; height: 420px;
    background: radial-gradient(closest-side, rgba(226,180,58,.55), rgba(226,180,58,0)); }
  .decor-stars-right { right: 0; top: 0; width: 110px; height: 480px;
    background: radial-gradient(closest-side, rgba(226,180,58,.55), rgba(226,180,58,0)); }
  .decor-gifts-left { left: 0; bottom: 0; width: 232px; height: 420px;
    background: radial-gradient(ellipse 100% 80% at 30% 100%, var(--gift) 0%, var(--gift) 45%, rgba(226,180,58,.35) 70%, rgba(226,180,58,0) 100%); }
  .decor-gifts-right { right: 0; bottom: 0; width: 232px; height: 420px;
    background: radial-gradient(ellipse 100% 80% at 70% 100%, var(--gift) 0%, var(--gift) 45%, rgba(226,180,58,.35) 70%, rgba(226,180,58,0) 100%); }
  .headline { position: absolute; left: 0; width: 100%; line-height: 1; color: var(--silver);
    text-shadow: 0 5px 0 var(--red-deep), 0 7px 10px rgba(0,0,0,.3); }
  .headline-top { top: 196px; font-size: 134px; letter-spacing: 1px; }
  .headline-bottom { top: 306px; font-size: 114px; }
  .headline .discount { color: var(--gold); }
  .hours-ribbon { position: absolute; left: 80px; top: 439px; width: 660px; height: 82px; }
  .hours-text { position: absolute; left: 126px; top: 439px; width: 568px; height: 54px;
    font-size: 44px; line-height: 56px; color: var(--ink); }
  .coupon-note { position: absolute; top: 526px; left: 0; width: 100%;
    font-family: "Montserrat", sans-serif; font-weight: 700; font-size: 30px; line-height: 38px;
    color: var(--white); letter-spacing: 1px; }
  .gift-band { position: absolute; left: 0; top: 610px; width: 100%; height: 121px;
    background: linear-gradient(90deg, var(--gold-dark), var(--gold) 20%, var(--gold-light) 50%, var(--gold) 80%, var(--gold-dark));
    color: var(--ink); padding-top: 12px; }
  .gift-band-title { font-size: 60px; line-height: 58px; }
  .gift-band-sub { font-size: 38px; line-height: 40px; }
  .extras { position: absolute; top: 748px; left: 0; width: 100%; }
  .extras-title { font-family: "Oswald", sans-serif; font-weight: 600; font-size: 36px; line-height: 44px;
    color: var(--white); transform: scaleX(.82); }
  .toy-drive { font-family: "Oswald", sans-serif; font-weight: 500; font-size: 30px; line-height: 42px;
    color: var(--gold); letter-spacing: 2px; transform: scaleX(.82); }
  .divider { position: absolute; left: 210px; top: 952px; width: 400px; height: 2px; background: rgba(255,255,255,.7); }
  .contact { position: absolute; left: 232px; top: 962px; width: 356px; color: var(--white);
    font-family: "Oswald", sans-serif; font-weight: 500; font-style: normal; }
  .contact-line { font-size: 22px; line-height: 30px; transform: scaleX(.78); white-space: nowrap; }
  .contact-phone { font-size: 40px; line-height: 48px; transform: scaleX(.82); }
  .brand-mark { margin-top: 6px; display: inline-flex; align-items: center; gap: 8px;
    font-family: "Oswald", sans-serif; font-weight: 500; font-size: 22px; color: var(--gold); }
  .brand-mark::before { content: ""; width: 12px; height: 12px; border-radius: 50%; background: var(--gold); }
</style>
</head>
<body>
  <main class="flyer">
    <div class="decor decor-stars-left" role="img" aria-label="Gold stars and faint snowflakes"></div>
    <div class="decor decor-stars-right" role="img" aria-label="Gold stars and sparkles"></div>
    <div class="decor decor-gifts-left" role="img" aria-label="Wrapped white gift boxes with red bows and gold foliage"></div>
    <div class="decor decor-gifts-right" role="img" aria-label="Wrapped white gift boxes with red bows and gold foliage"></div>

    <h1 class="headline headline-top">ENTIRE STORE</h1>
    <p class="headline headline-bottom">WILL BE <span class="discount">30% OFF</span></p>

    <svg class="hours-ribbon" viewBox="0 0 660 82" aria-hidden="true">
      <defs>
        <linearGradient id="ribbonGold" x1="0" x2="1">
          <stop offset="0" stop-color="#b98a1e"/><stop offset=".5" stop-color="#fbe38a"/><stop offset="1" stop-color="#b98a1e"/>
        </linearGradient>
      </defs>
      <polygon points="0,30 46,30 46,82 8,82 24,56" fill="#c99a2a"/>
      <polygon points="660,30 614,30 614,82 652,82 636,56" fill="#c99a2a"/>
      <polygon points="46,54 46,82 80,54" fill="#7a5a10"/>
      <polygon points="614,54 614,82 580,54" fill="#7a5a10"/>
      <rect x="46" y="0" width="568" height="54" fill="url(#ribbonGold)"/>
    </svg>
    <p class="hours-text">FRIDAY HOURS: 9-6 &nbsp;|&nbsp; SATURDAY: 9-4</p>

    <p class="coupon-note">Each customer will receive a<br>coupon for December 1-24.</p>

    <section class="gift-band">
      <p class="gift-band-title">FIRST 25 CUSTOMERS EACH DAY</p>
      <p class="gift-band-sub">WILL RECEIVE A SURPRISE GIFT VALUED AT $50+</p>
    </section>

    <section class="extras">
      <p class="extras-title">TONS OF GIVEAWAYS, FOOD &amp; DRINKS!</p>
      <p class="toy-drive">BRING/BUY AN UNOPENED TOY FOR PINECREST<br>MUTUAL AID &amp; RECEIVE A $10 GIFT CARD.</p>
    </section>

    <div class="divider"></div>
    <address class="contact">
      <p class="contact-line">CLOVERPATCH CRADLE</p>
      <p class="contact-line">FERNHOLLOW, WA</p>
      <p class="contact-line">HALVORN PLAZA CENTER : NEXT TO TALL OATS</p>
      <p class="contact-phone">(555) 201-4938</p>
      <span class="brand-mark">Cloverpatch Cradle</span>
    </address>
  </main>
</body>
</html>
```